Introduction of new dentist and new treatments

We want inform our Patients of our new dentist and new treatment methods. It is dealing about biologic dentistry and holistic dentistry. we are in switzerland and speak german

Font styles to use
Sans Serif

Colors
00a990
33b8a4
9bcb3c
acd036
cadf82
0292cd
3176b5
e34297
e667a6

Requirements
Must have
• Text, which can be edited. It will be in german
• Name of the dental clinic is
• "Brivana - Ihr Zahnarzt in Zug"
Nice to have
• A4 Layout

```html
<!DOCTYPE html>
<html lang="de">
<head>
<meta charset="utf-8">
<title>Brivana – Interdisziplinäre Zahnmedizin</title>
<link href="https://fonts.googleapis.com/css2?family=Roboto+Condensed:wght@700&family=Ubuntu:wght@400;500&family=Roboto:wght@400;700&display=swap" rel="stylesheet">
<style>
  :root {
    --pink: #e34297;
    --pink-deep: #d6337f;
    --pink-soft: #e667a6;
    --blue: #3176b5;
    --blue-bright: #0292cd;
    --band: #b9dbe4;
    --green-line: #cadf82;
    --paper: #f8f8f5;
    --ink: #1f1f24;
    --navy: #26305a;
    --backdrop: #e6e6e4;
  }
  html, body {
    margin: 0;
    width: 1200px;
    height: 1200px;
    overflow: hidden;
    background: var(--backdrop);
  }
  .flyer {
    position: absolute;
    left: 181px;
    top: 36px;
    width: 838px;
    height: 1128px;
    background: var(--paper);
    overflow: hidden;
    box-shadow: 0 6px 24px rgba(0,0,0,.18);
  }
  .flyer-header, .flyer-footer {
    position: absolute;
    left: 0;
    width: 838px;
  }
  .flyer-header { top: 0; height: 260px; }
  .flyer-footer { bottom: 0; height: 80px; }
  .brand {
    position: absolute;
    left: 143px;
    width: 200px;
    top: 238px;
    text-align: center;
    font-family: "Ubuntu", sans-serif;
    color: var(--navy);
  }
  .brand-mark {
    display: block;
    width: 14px;
    height: 14px;
    margin: 0 auto 10px;
    border-radius: 50%;
    background: var(--pink-soft);
  }
  .brand-name {
    font-size: 21px;
    font-weight: 400;
    letter-spacing: 4px;
    text-transform: uppercase;
  }
  .brand-tagline {
    font-size: 10.5px;
    font-weight: 500;
    margin-top: 4px;
  }
  .content {
    position: absolute;
    left: 66px;
    top: 326px;
    width: 704px;
    font-family: "Ubuntu", sans-serif;
    color: var(--ink);
  }
  .title {
    margin: 0;
    font-family: "Roboto Condensed", sans-serif;
    font-weight: 700;
    font-size: 34px;
    color: var(--pink-deep);
    line-height: 1.1;
  }
  .subtitle {
    margin: 4px 0 20px;
    font-family: "Roboto Condensed", sans-serif;
    font-weight: 700;
    font-size: 20.5px;
    color: var(--ink);
    line-height: 1.2;
  }
  .content p {
    margin: 0;
    font-size: 13.2px;
    line-height: 20.6px;
    text-align: justify;
  }
  .section-heading {
    margin: 21px 0 0;
    font-size: 14.5px;
    font-weight: 500;
    line-height: 20px;
  }
  .section-heading.is-blue { color: var(--blue); }
  .section-heading.is-pink { color: var(--pink-deep); }
  .call {
    position: absolute;
    right: 66px;
    bottom: 22px;
    font-family: "Roboto", sans-serif;
    color: #fff;
    font-size: 20px;
  }
  .call strong { font-size: 24px; font-weight: 700; letter-spacing: .5px; }
</style>
</head>
<body>
  <article class="flyer">
    <svg class="flyer-header" viewBox="0 0 838 260" aria-hidden="false">
      <defs>
        <linearGradient id="pinkField" x1="0" y1="0" x2="1" y2="1">
          <stop offset="0" stop-color="#d9347f"/>
          <stop offset=".6" stop-color="#e34297"/>
          <stop offset="1" stop-color="#e667a6"/>
        </linearGradient>
        <linearGradient id="portraitTone" x1="0" y1="0" x2="0" y2="1">
          <stop offset="0" stop-color="#e78fb4"/>
          <stop offset=".55" stop-color="#d9a08e"/>
          <stop offset="1" stop-color="#2f66b0"/>
        </linearGradient>
      </defs>
      <rect class="header-field" width="838" height="260" fill="url(#pinkField)"/>
      <rect class="portrait" x="560" y="14" width="260" height="240" rx="6" fill="url(#portraitTone)" opacity=".75" role="img" aria-label="Porträtfoto des neuen Zahnarztes im blauen Poloshirt"/>
      <path class="header-band" d="M0 98 C160 80 300 120 450 180 C600 240 720 250 838 236 L838 260 L0 260 Z" fill="var(--band)"/>
      <path class="header-paper" d="M0 138 C170 110 320 140 460 200 C590 252 720 256 838 244 L838 260 L0 260 Z" fill="var(--paper)"/>
    </svg>

    <div class="brand">
      <span class="brand-mark"></span>
      <div class="brand-name">Brivana</div>
      <div class="brand-tagline">Ihr Zahnarzt in Zug</div>
    </div>

    <main class="content">
      <h1 class="title">Interdisziplinäre Zahnmedizin</h1>
      <h2 class="subtitle">Zusammenhang zwischen Zahnproblemen und der Gesundheit von Körper und Geist</h2>
      <p>Zahn und Gesundheit haben eins gemeinsam – Man vermisst sie, wenn sie fehlt. Zähne haben einen engen Zusammenhang zur Gesundheit und können diese beeinflussen. Sowohl negativ als auch positiv.</p>

      <h3 class="section-heading is-blue">Funktion des Kauorgans und interdisziplinäre Zahnmedizin</h3>
      <p>„Funktion ist nicht alles. Aber ohne Funktion ist alles nichts!“ Sagte einst Prof. A. Lindqvist (Zahnarzt, Gnathologie) und betonte die Bedeutung der Funktion des Kausystems. Sprechen, Kauen aber auch Körperhaltung und Stressmanagement gehören zu den Funktionen der Zähne. Ein gut funktionierendes Kauorgan (nach Prof. R. Marenko, interdisziplinäre Zahnmedizin) kann Stress bewältigen und mehr Leistung und Wohlbefinden bringen. Sehr oft erkennt man Funktionsstörungen daran, dass die Zähne nicht richtig zueinander passen oder Muskelverspannungen und Schmerzen im Kiefergelenk auftreten.</p>

      <h3 class="section-heading is-pink">Parodontitis und systemische Erkrankungen</h3>
      <p>Parodontitis (Entzündung des Zahnhalteapparats) ist eine der häufigsten chronischen Krankheiten weltweit und daher gut erforscht. Herzkrankheiten, Diabetes und Frühgeburtlichkeit sind einige der systemischen Krankheiten mit der Parodontitis in Zusammenhang steht. Zahnfleischbluten, Zahnlockerung, Zahnfleischschwund und Zahnverlust sind typische Begleiterscheinungen von Parodontitis. Eine systematische Parodontitis-Behandlung kann auch positive Auswirkungen auf die gesamte Gesundheit haben.</p>

      <h3 class="section-heading is-blue">Zahnverlust und neurologische Auswirkung</h3>
      <p>Ein physiologisches Kausystem hat sehr feine Steuerungs- und Wahrnehmungsmöglichkeiten. Bei Zahnverlust werden diese Fähigkeiten weniger benötigt. Weniger gebrauchte Ressourcen werden von der Natur dementsprechend abgebaut. Studien zeigen, dass Menschen mit weniger Zähnen mehr Risiko zur Bildung von Demenz bergen.</p>

      <h3 class="section-heading is-pink">Ganzheitliche Erklärungen</h3>
      <p>Die komplementäre Zahnheilkunde, sehr oft auch als ganzheitliche oder biologische Zahnheilkunde bezeichnet, versucht mit Hilfe von Meridianen (Traditionelle Chinesische Medizin), den Zusammenhang zwischen Zähnen und anderen Organen und Körperteilen zu erklären. Es gibt immer mehr Patienten und Zahnärzte die von dieser Theorie und deren Ergebnissen überzeugt sind. Aufgrund der wissenschaftlichen Lage ist eine ausführliche Aufklärung vor der Behandlung sehr ratsam.</p>
    </main>

    <svg class="flyer-footer" viewBox="0 0 838 80" aria-hidden="true">
      <path class="footer-line" d="M0 50 C260 20 520 -2 838 14" fill="none" stroke="var(--green-line)" stroke-width="3"/>
      <path class="footer-band" d="M0 52 C260 24 520 2 838 18 L838 80 L0 80 Z" fill="var(--blue)"/>
      <path class="footer-edge" d="M0 70 C300 60 560 62 838 66 L838 80 L0 80 Z" fill="#2a63a4"/>
    </svg>
    <div class="call">Call: <strong>+41 41 000 12 34</strong></div>
  </article>
</body>
</html>
```